Business Card Design

Business Card for professional consulting firm working with large financial institutions.

Target Market(s)

Executive buyers

Industry/Entity Type

Banking

Contact Information for Business Card

Mild creativity wanted. Not boring, but do elaborate artwork.

Font styles to use
Serif
Sans Serif

Colors

Designer to choose colors to be used in the design.

Requirements
Must have
• Standard business card features - company name, individual name, telephone, website, email, locations.
Nice to have
• Two colors
Should not have
• too many colors, fancy printing, cartoons.

```html
<!DOCTYPE html>
<html lang="en">
<head>
<meta charset="utf-8">
<title>Keymeridian Business Card</title>
<link rel="stylesheet" href="https://fonts.googleapis.com/css2?family=Noto+Serif&family=Arimo:wght@400;700&display=swap">
<style>
  :root {
    --stage: #2b2b2b;
    --card-dark: #111111;
    --card-light: #f4f4f4;
    --card-light-edge: #dcdcdc;
    --ink: #1a1a1a;
    --ink-soft: #555555;
    --rule: #8a8a8a;
    --accent-grey: #a4a4a4;
    --accent-grey-deep: #8c8c8c;
    --paper-white: #ffffff;
  }
  * { box-sizing: border-box; margin: 0; padding: 0; }
  html, body { width: 1200px; height: 997px; overflow: hidden; }
  body {
    background: var(--stage);
    position: relative;
    font-family: "Arimo", Arial, sans-serif;
  }
  .card {
    position: absolute;
    width: 520px;
    height: 297px;
    top: 350px;
    border-radius: 3px;
    overflow: hidden;
  }
  .card--back { left: 50px; background: var(--card-dark); }
  .card--front {
    left: 630px;
    background: linear-gradient(180deg, var(--paper-white) 0%, var(--card-light) 60%, var(--card-light-edge) 100%);
  }
  .brand-name {
    font-family: "Noto Serif", Georgia, serif;
    letter-spacing: 0.5px;
    position: absolute;
  }
  .card--back .brand-name {
    color: var(--paper-white);
    font-size: 44px;
    left: 0; right: 0; top: 118px;
    text-align: center;
  }
  .card--front .brand-name {
    color: var(--ink);
    font-size: 38px;
    left: 150px; top: 40px;
  }
  .card-shapes { position: absolute; inset: 0; }
  .holder {
    position: absolute;
    left: 30px; top: 158px;
  }
  .holder-name { font-weight: 700; font-size: 16px; line-height: 18px; color: var(--ink); }
  .holder-role { font-size: 14px; color: var(--ink-soft); margin-top: 3px; }
  .contact-list { list-style: none; position: absolute; left: 30px; top: 200px; }
  .contact-list li {
    display: flex; align-items: center; gap: 10px;
    font-size: 15px; color: var(--ink); margin-bottom: 6px;
  }
  .contact-icon { width: 14px; height: 14px; }
  .office {
    position: absolute; right: 22px; top: 108px;
    text-align: right; font-size: 13px; line-height: 17px; color: var(--ink-soft);
  }
  .office-name { font-weight: 700; color: var(--ink); }
  .website {
    position: absolute; right: 22px; top: 236px;
    font-weight: 700; font-size: 14px; color: var(--paper-white);
  }
</style>
</head>
<body>

<section class="card card--back" aria-label="Card back">
  <p class="brand-name">keymeridian</p>
</section>

<section class="card card--front" aria-label="Card front">
  <svg class="card-shapes" width="520" height="297" viewBox="0 0 520 297">
    <defs>
      <linearGradient id="swoosh-fill" x1="0" y1="0" x2="1" y2="0">
        <stop offset="0" stop-color="var(--accent-grey)"/>
        <stop offset="1" stop-color="var(--accent-grey-deep)"/>
      </linearGradient>
    </defs>
    <line x1="160" y1="100" x2="500" y2="100" stroke="var(--rule)" stroke-width="1"/>
    <line x1="128" y1="172" x2="500" y2="172" stroke="var(--rule)" stroke-width="1"/>
    <path d="M520,222 L352,222 C334,222 328,230 324,244 L318,265 L520,265 Z" fill="var(--card-dark)"/>
    <path d="M0,258 C110,254 220,246 300,238 C312,237 320,238 322,242 L320,248 C230,254 120,262 0,268 Z" fill="url(#swoosh-fill)"/>
    <rect x="0" y="280" width="520" height="5" fill="var(--card-light-edge)"/>
  </svg>

  <p class="brand-name">keymeridian</p>

  <div class="office">
    <p class="office-name">KEYMERIDIAN PVT LTD</p>
    <p>2200 Harbor Point Dr,Suite 300</p>
    <p>Austin Tx 78701</p>
  </div>

  <div class="holder">
    <p class="holder-name">Lena Marsh</p>
    <p class="holder-role">Director</p>
  </div>

  <ul class="contact-list">
    <li>
      <svg class="contact-icon" viewBox="0 0 14 14" aria-hidden="true">
        <circle cx="7" cy="7" r="7" fill="var(--ink-soft)"/>
        <path d="M4,5 Q7,3 10,5 L9,6 L5,6 Z M4.5,7 H9.5 V10 H4.5 Z" fill="var(--paper-white)"/>
      </svg>
      <span>555-014-2277</span>
    </li>
    <li>
      <svg class="contact-icon" viewBox="0 0 14 14" aria-hidden="true">
        <circle cx="7" cy="7" r="7" fill="var(--ink-soft)"/>
        <rect x="3.5" y="4.5" width="7" height="5" fill="none" stroke="var(--paper-white)" stroke-width="1"/>
        <path d="M3.5,4.5 L7,7.5 L10.5,4.5" fill="none" stroke="var(--paper-white)" stroke-width="1"/>
      </svg>
      <span>Lena@keymeridian.com</span>
    </li>
  </ul>

  <p class="website">www.keymeridian.com</p>
</section>

</body>
</html>
```